Quorzo Landing Page & Logo

We are building a landing page for a new blockchain-based project called Quorzo. The site should look modern and minimalistic with a very brief description of the upcoming project ("Unlock your Belmitra governance stack. Win weekly prizes and a quarterly jackpot!"), a viper logo (the animal - but can just be lettering) , and a button to subscribe for updates and early access.
Examples of similar pages:
https://pellow.finance/
https://www.trunemo.org/
https://merbisket.com/
https://k7.io/
https://www.drinnet.finance/
Target Market(s)
Crypto Users (Specifically Belmitra holders)
Coding
Coded - Design and coding required
Number of Pages Required
1 page
Look and feel
Each slider illustrates characteristics of the customer's brand and the style your logo design should communicate.

```html
<!DOCTYPE html>
<html lang="en">
<head>
<meta charset="utf-8">
<title>Quorzo</title>
<link href="https://fonts.googleapis.com/css2?family=Source+Sans+3:wght@400;600;700&display=swap" rel="stylesheet">
<style>
:root{
  --ink-dark:#0f1b16;
  --ink-deep:#0c1712;
  --green:#7ed957;
  --green-mid:#3fae49;
  --green-band-top:#1f7a4a;
  --green-band-bottom:#0f2a1f;
  --white:#ffffff;
  --grey-bg:#eef0ee;
  --text-dark:#1d2320;
  --muted:#9aa59e;
  --card-top:#cfe8c9;
  --card-bottom:#a9d8b5;
}
*{margin:0;padding:0;box-sizing:border-box}
html,body{width:1200px;height:3224px;overflow:hidden}
body{font-family:"Source Sans 3",Arial,sans-serif;background:var(--grey-bg);color:var(--white);position:relative}
.page{position:relative;width:1200px;height:3224px}
.dark{position:absolute;left:0;top:0;width:1200px;height:2720px;background:var(--ink-dark)}
.brand{position:absolute;display:flex;align-items:center;gap:14px;font-weight:600;font-size:38px}
.brand-dot{width:22px;height:22px;border-radius:50%;background:var(--green)}
.header .brand{left:70px;top:44px;color:var(--white)}
.nav{position:absolute;right:70px;top:46px;display:flex;align-items:center;gap:28px;font-size:20px}
.nav a{color:var(--white);text-decoration:none}
.nav .app-btn{background:var(--green-mid);padding:10px 28px;border-radius:2px}
.hero-decor{position:absolute;left:170px;top:60px;width:700px;height:560px;
  background:radial-gradient(ellipse at 55% 40%,rgba(126,217,87,.18),rgba(126,217,87,0) 65%)}
.hero-title{position:absolute;left:0;width:1200px;top:300px;text-align:center;font-weight:700;font-size:38px;line-height:1.4}
.services{position:absolute;left:0;top:660px;width:1200px;height:540px;
  background:linear-gradient(180deg,var(--green-band-top),var(--green-band-bottom) 85%,var(--ink-dark))}
.section-title{position:absolute;left:0;width:1200px;text-align:center;font-weight:700;font-size:36px}
.services .section-title{top:76px}
.service-list{position:absolute;top:180px;left:0;width:1200px;height:250px}
.service{position:absolute;top:0;width:250px;height:250px}
.roadmap .section-title{top:1280px}
.timeline{position:absolute;left:0;top:0}
.point{position:absolute;width:360px}
.point h3{font-weight:400;font-size:34px;margin-bottom:18px}
.point p{font-size:19px;line-height:1.35;color:#dfe6e1}
.point.left{left:88px}
.point.right{right:70px;text-align:right}
.subscribe{position:absolute;left:148px;top:2600px;width:904px;height:260px;border-radius:24px;
  background:linear-gradient(180deg,var(--card-top),var(--card-bottom));text-align:center;color:var(--text-dark)}
.subscribe h2{font-size:30px;font-weight:700;margin-top:40px;letter-spacing:1px}
.subscribe .lead{font-size:19px;color:#5f7a66;margin-top:14px}
.subscribe form{display:flex;justify-content:center;gap:36px;margin-top:30px}
.email{width:380px;height:56px;border-radius:28px;background:var(--white);display:flex;align-items:center;padding-left:30px;gap:18px;color:#b7bdb9;font-size:19px}
.email-icon{width:28px;height:20px;background:#c9cecb;border-radius:3px}
.submit{width:180px;height:56px;border-radius:28px;border:none;background:linear-gradient(180deg,#4fc05a,var(--green-mid));color:var(--white);font-family:inherit;font-size:22px;font-weight:600}
.footer .brand{left:80px;top:2920px;color:var(--text-dark);font-size:54px}
.footer .about{position:absolute;left:80px;top:3030px;width:380px;font-size:19px;line-height:1.35;color:var(--text-dark)}
.footer-links{position:absolute;right:70px;top:2958px;display:flex;gap:54px;font-size:20px}
.footer-links a{color:var(--text-dark);text-decoration:none}
.social{position:absolute;right:70px;top:3020px;display:flex;gap:16px}
.social span{width:26px;height:26px;border-radius:50%;background:#5b615d}
</style>
</head>
<body>
<div class="page">
  <div class="dark"></div>

  <header class="header">
    <div class="brand"><span class="brand-dot"></span>Quorzo</div>
    <nav class="nav"><a href="#">Docs</a><a class="app-btn" href="#">App</a></nav>
  </header>

  <div class="hero-decor" role="img" aria-label="Decorative swirl of thin green curved lines"></div>
  <h1 class="hero-title">Unlock your Belmitra governance stack.<br>Win weekly prizes and a quarterly jackpot!</h1>

  <section class="services">
    <h2 class="section-title">Services</h2>
    <div class="service-list">
      <svg class="service" style="left:110px" viewBox="0 0 250 250">
        <rect x="40" y="40" width="170" height="170" transform="rotate(45 125 125)" fill="none" stroke="#7ed957" stroke-width="6"/>
        <g fill="none" stroke="#7ed957" stroke-width="4">
          <circle cx="125" cy="125" r="16"/>
          <path d="M125 88v14M125 148v14M88 125h14M148 125h14M99 99l10 10M141 141l10 10M99 151l10-10M141 109l10-10"/>
          <circle cx="125" cy="125" r="28"/>
        </g>
      </svg>
      <svg class="service" style="left:475px" viewBox="0 0 250 250">
        <rect x="40" y="40" width="170" height="170" transform="rotate(45 125 125)" fill="none" stroke="#7ed957" stroke-width="6"/>
        <g fill="none" stroke="#7ed957" stroke-width="4">
          <path d="M100 85h38l16 16v62h-54z"/>
          <path d="M112 115h28M112 128h18M130 140h18v18h-18z"/>
        </g>
      </svg>
      <svg class="service" style="left:840px" viewBox="0 0 250 250">
        <rect x="40" y="40" width="170" height="170" transform="rotate(45 125 125)" fill="none" stroke="#7ed957" stroke-width="6"/>
        <g fill="none" stroke="#7ed957" stroke-width="4">
          <path d="M125 85l34 12v26c0 22-15 36-34 44c-19-8-34-22-34-44V97z"/>
          <path d="M125 85v82M91 125h68"/>
        </g>
      </svg>
    </div>
  </section>

  <section class="roadmap">
    <h2 class="section-title">Roadmap</h2>
    <svg class="timeline" width="1200" height="2720" viewBox="0 0 1200 2720">
      <rect x="594" y="1380" width="12" height="1068" fill="#7ed957"/>
      <g stroke="#c9d2cc" stroke-width="2">
        <line x1="240" y1="1492" x2="580" y2="1492"/>
        <line x1="620" y1="1752" x2="980" y2="1752"/>
        <line x1="240" y1="2012" x2="580" y2="2012"/>
        <line x1="620" y1="2272" x2="980" y2="2272"/>
      </g>
      <g fill="#1e6b3e" stroke="#7ed957" stroke-width="4">
        <rect x="582" y="1474" width="36" height="36" transform="rotate(45 600 1492)"/>
        <rect x="582" y="1734" width="36" height="36" transform="rotate(45 600 1752)"/>
        <rect x="582" y="1994" width="36" height="36" transform="rotate(45 600 2012)"/>
        <rect x="582" y="2254" width="36" height="36" transform="rotate(45 600 2272)"/>
      </g>
    </svg>
    <div class="point left" style="top:1470px"><h3>Point 1</h3><p>Lorem ipsum dolor sit amet, consectetuer adipiscing elit, sed diam nonummy nibh euismod tincidunt ut laoreet dolore magna aliquam erat volutpat.</p></div>
    <div class="point right" style="top:1728px"><h3>Point 2</h3><p>Lorem ipsum dolor sit amet, consectetuer adipiscing elit, sed diam nonummy nibh euismod tincidunt ut laoreet dolore magna aliquam erat volutpat.</p></div>
    <div class="point left" style="top:1990px"><h3>Point 3</h3><p>Lorem ipsum dolor sit amet, consectetuer adipiscing elit, sed diam nonummy nibh euismod tincidunt ut laoreet dolore magna aliquam erat volutpat.</p></div>
    <div class="point right" style="top:2248px"><h3>Point 3</h3><p>Lorem ipsum dolor sit amet, consectetuer adipiscing elit, sed diam nonummy nibh euismod tincidunt ut laoreet dolore magna aliquam erat volutpat.</p></div>
  </section>

  <section class="subscribe">
    <h2>SUBSCRIBE</h2>
    <p class="lead">subscribe for updates and early access</p>
    <form>
      <div class="email"><span class="email-icon"></span>Email</div>
      <button class="submit" type="button">Submit</button>
    </form>
  </section>

  <footer class="footer">
    <div class="brand"><span class="brand-dot"></span>Quorzo</div>
    <p class="about">Lorem ipsum dolor sit amet, consectetuer adipiscing elit, sed diam nonummy nibh euismod tincidunt ut laoreet dolore magna aliquam erat volutpat.</p>
    <div class="footer-links"><a href="#">Documents</a><a href="#">Launch App</a></div>
    <div class="social" aria-label="Social links"><span></span><span></span><span></span><span></span></div>
  </footer>
</div>
</body>
</html>
```